依頼詳細
残暑お見舞い申し上げます

コロナ禍と暑さで汗が噴き出るような日々が続きますが、いかがお過ごしでしょうか?
汗はかけばかくほど、老廃物が体内から出て、心も体も健康になります。
汗をかかないようにすることは、決して良いことではありません。
会社にとっても、今年は汗(特別損失)を出せるチャンスです。
個人も会社もたくさんの汗を出して、より健康体になられること、心より祈念申し上げます。

★写真に添える文章:松本清志の最新刊
「伸びる会社へ組み直す」
定価10,780円(税込み)
記載項目
ノルフェン・パートナーズ
松本 清志・長谷 宗一郎・柴田 昌平
希望イメージ
シンプル 複雑
単色 カラフル
暗い 明るい
日常 高級
遊び心 厳粛
未来的 伝統的
女性的 男性的
希望する色
水色系
納品ファイル
• 高解像度JPG (.jpg)
補足説明
■ 選んだ理由

今年はコロナのイベント中止で花火大会もなくなるなかで、
もってこいのデザインでした。
文字の並べ方に工夫が見られ、メッセージとバックのコントラストが素敵でした。
一目見ておしゃれで気に入りました。

■ 提案者全員のお礼・コメント

この度は、ご応募ありがとうございました。
毎回、新たなご提案が来るのが楽しみでした。素敵なご応募をありがとうございました。

```html
<!DOCTYPE html>
<html lang="ja">
<head>
<meta charset="utf-8">
<title>残暑お見舞い申し上げます</title>
<link rel="stylesheet" href="https://fonts.googleapis.com/css2?family=Noto+Serif+JP:wght@300;400;600&family=Noto+Sans+JP:wght@500;700&display=swap">
<style>
  :root {
    --paper: #ffffff;
    --sky: #cfe9f5;
    --sky-soft: #e9f5fb;
    --leaf: #bfe0c4;
    --ink: #2f2f2f;
    --ink-soft: #444444;
    --book-red: #b3262a;
    --book-dark: #3a1d1a;
  }
  html, body {
    margin: 0;
    padding: 0;
    width: 809px;
    height: 1200px;
    overflow: hidden;
    background: var(--paper);
  }
  .card {
    position: relative;
    width: 809px;
    height: 1200px;
    background: var(--paper);
    font-family: "Noto Serif JP", serif;
    color: var(--ink);
    overflow: hidden;
  }
  .summer-sky {
    position: absolute;
    inset: 0 0 auto 0;
    height: 360px;
    background:
      radial-gradient(ellipse 60% 55% at 20% 15%, var(--leaf) 0%, rgba(191,224,196,0) 70%),
      radial-gradient(ellipse 55% 50% at 85% 10%, var(--sky) 0%, rgba(207,233,245,0) 75%),
      linear-gradient(180deg, var(--sky-soft) 0%, rgba(255,255,255,0) 100%);
  }
  .vertical {
    position: absolute;
    writing-mode: vertical-rl;
    text-orientation: mixed;
    margin: 0;
  }
  .greeting-title {
    top: 165px;
    right: 62px;
    font-size: 60px;
    font-weight: 300;
    letter-spacing: 0.12em;
    line-height: 1;
  }
  .message {
    top: 310px;
    right: 182px;
    font-size: 19px;
    line-height: 28px;
    letter-spacing: 0.04em;
    font-weight: 400;
  }
  .message span { display: block; }
  .signature {
    top: 310px;
    right: 395px;
    font-size: 19px;
    line-height: 40px;
    letter-spacing: 0.06em;
  }
  .signature .date { display: block; padding-top: 470px; }
  .signature .company,
  .signature .names { display: block; }
  .new-book {
    position: absolute;
    left: 40px;
    top: 735px;
    width: 165px;
  }
  .book-cover {
    width: 165px;
    height: 300px;
    background: linear-gradient(160deg, var(--book-red) 0%, #8e1c20 55%, var(--book-dark) 100%);
    box-shadow: 3px 4px 8px rgba(0,0,0,0.25);
  }
  .book-caption {
    margin-top: 18px;
    font-family: "Noto Sans JP", sans-serif;
    text-align: center;
    color: var(--ink-soft);
    font-size: 12px;
    line-height: 1.6;
  }
  .book-caption .lead { font-weight: 700; font-size: 14px; color: var(--ink); }
</style>
</head>
<body>
  <main class="card">
    <div class="summer-sky" role="img" aria-label="風鈴が吊り下がり、青葉が揺れる夏空のイラスト"></div>

    <h1 class="vertical greeting-title">残暑お見舞い申し上げます</h1>

    <p class="vertical message">
      <span>コロナ禍と暑さで汗が噴き出るような日々が続きますが、</span>
      <span>いかがお過ごしでしょうか？</span>
      <span>汗はかけばかくほど、老廃物が体内から出て、心も体も健康になります。</span>
      <span>汗をかかないようにすることは、決して良いことではありません。</span>
      <span>会社にとっても、今年は汗（特別損失）を出せるチャンスです。</span>
      <span>個人も会社もたくさんの汗を出して、より健康体になられること、</span>
      <span>心より祈念申し上げます。</span>
    </p>

    <p class="vertical signature">
      <span class="date">令和二年　晩夏</span>
      <span class="company">ノルフェン・パートナーズ</span>
      <span class="names">松本 清志・長谷 宗一郎・柴田 昌平</span>
    </p>

    <aside class="new-book">
      <div class="book-cover" role="img" aria-label="新刊『伸びる会社へ組み直す』の書籍表紙写真"></div>
      <div class="book-caption">
        <div class="lead">松本清志の最新刊</div>
        <div>「伸びる会社へ組み直す」</div>
        <div>定価10,780円（税込）</div>
      </div>
    </aside>
  </main>
</body>
</html>
```